Create a Business Card

I am a Real Estate Professional based in Miami FL. I work for Silver Harbor Realty. I am looking for a classy, sharp, elegant eye catching business card design with my headshot and information. The business cards will be on a thick plastic material (Like a credit card feel).,

This is the info I would like on the card:

Kellan Ostrowe P.A.
Silver Harbor Realty
(555) 814-2706
KOstrowerealtor@[login to view URL]
Instagram - @Siha_Kellan

```html
<!DOCTYPE html>
<html lang="en">
<head>
<meta charset="utf-8">
<title>Kellan Ostrowe P.A. — Business Card</title>
<link href="https://fonts.googleapis.com/css2?family=Montserrat:wght@400;500;600;700;800&display=swap" rel="stylesheet">
<style>
  :root {
    --canvas: #e9e7e3;
    --card: #2a2a2b;
    --card-edge: #232324;
    --green: #2fb34a;
    --white: #f2f2f2;
    --rule: #b9b9b9;
    --photo-a: #3b5a86;
    --photo-b: #c7a48a;
  }
  * { box-sizing: border-box; margin: 0; padding: 0; }
  html, body { width: 1200px; height: 800px; overflow: hidden; }
  body {
    background: var(--canvas);
    font-family: "Montserrat", sans-serif;
    position: relative;
  }
  .card {
    position: absolute;
    top: 250px;
    width: 525px;
    height: 300px;
    background: var(--card);
    border-radius: 10px;
    box-shadow: 0 10px 30px rgba(0,0,0,.25);
    overflow: hidden;
  }
  .card--front { left: 50px; }
  .card--back { left: 625px; }

  /* front */
  .front-brand {
    position: absolute;
    left: 150px;
    top: 92px;
    display: flex;
    align-items: center;
    gap: 14px;
  }
  .front-brand__dot {
    width: 16px; height: 16px;
    border-radius: 50%;
    background: var(--green);
  }
  .front-brand__name {
    color: var(--white);
    font-weight: 700;
    font-size: 26px;
    line-height: 1.05;
    letter-spacing: .5px;
    text-transform: uppercase;
  }
  .front-rule {
    position: absolute;
    left: 0;
    top: 242px;
    width: 100%;
    height: 20px;
  }
  .front-web {
    position: absolute;
    top: 243px;
    left: 0;
    width: 100%;
    text-align: center;
    color: var(--green);
    font-size: 13px;
    font-weight: 500;
  }

  /* back */
  .headshot {
    position: absolute;
    left: 50%;
    top: 28px;
    transform: translateX(-50%);
    width: 100px; height: 100px;
    border-radius: 50%;
    border: 3px solid #d9d9d9;
    background: radial-gradient(circle at 50% 38%, var(--photo-b) 0 28%, var(--photo-a) 60%);
  }
  .back-info {
    position: absolute;
    left: 0; right: 0;
    top: 140px;
    text-align: center;
  }
  .agent-name {
    color: var(--green);
    font-weight: 800;
    font-size: 24px;
    letter-spacing: .5px;
    text-transform: uppercase;
  }
  .agent-company {
    margin-top: 2px;
    display: inline-flex;
    align-items: center;
    gap: 6px;
    color: var(--white);
    font-size: 10px;
    font-weight: 600;
    text-transform: uppercase;
  }
  .agent-company__dot {
    width: 8px; height: 8px;
    border-radius: 50%;
    background: var(--green);
  }
  .contact {
    margin-top: 12px;
    color: var(--green);
    font-size: 12px;
    line-height: 1.45;
    list-style: none;
  }
  .contact-icons {
    margin-top: 6px;
    display: flex;
    justify-content: center;
    gap: 8px;
  }
</style>
</head>
<body>

  <section class="card card--front" aria-label="Card front">
    <div class="front-brand">
      <span class="front-brand__dot"></span>
      <div class="front-brand__name">Silver Harbor<br>Realty</div>
    </div>
    <svg class="front-rule" viewBox="0 0 525 20" preserveAspectRatio="none">
      <line x1="0" y1="10" x2="170" y2="10" stroke="var(--rule)" stroke-width="3"/>
      <line x1="355" y1="10" x2="525" y2="10" stroke="var(--rule)" stroke-width="3"/>
    </svg>
    <p class="front-web">www.KellanOstrowe.com</p>
  </section>

  <section class="card card--back" aria-label="Card back">
    <div class="headshot" role="img" aria-label="Headshot of Kellan Ostrowe"></div>
    <div class="back-info">
      <h1 class="agent-name">Kellan Ostrowe P.A.</h1>
      <div class="agent-company"><span class="agent-company__dot"></span>Silver Harbor Realty</div>
      <ul class="contact">
        <li>(555) 814-2706</li>
        <li>KOstrowerealtor@harbormail.com</li>
        <li>@Siha_Kellan</li>
      </ul>
      <div class="contact-icons">
        <svg width="12" height="12" viewBox="0 0 12 12" aria-label="Phone">
          <rect x="3" y="1" width="6" height="10" rx="1.2" fill="none" stroke="var(--white)" stroke-width="1.2"/>
          <line x1="5" y1="9" x2="7" y2="9" stroke="var(--white)" stroke-width="1"/>
        </svg>
        <svg width="12" height="12" viewBox="0 0 12 12" aria-label="Email">
          <rect x="1" y="3" width="10" height="7" fill="none" stroke="var(--white)" stroke-width="1.2"/>
          <polyline points="1,3 6,7 11,3" fill="none" stroke="var(--white)" stroke-width="1.2"/>
        </svg>
        <svg width="12" height="12" viewBox="0 0 12 12" aria-label="Social handle">
          <rect x="1.5" y="1.5" width="9" height="9" rx="2" fill="none" stroke="var(--white)" stroke-width="1.2"/>
        </svg>
      </div>
    </div>
  </section>

</body>
</html>
```